Business Card Design

We need a business card design for a new company based in Melbourne Australia. We are financial broker in finance industry. We provide a wide range of finance solutions to our clients including home loans, commercial loans, business facilities, car loans, equipment loans, invoice finance, etc. The company name is from director's personal name. We would like to have a new company logo that includes TK.

Industry/Entity Type

Business

Contact Information for Business Card

company name: TK & Co Finance Pty Ltd
person's name: Desmond Okafor
role: Managing Director
Mobile: 0417 638 294
fax: 03 9561 4472
Email: desmond.okafor@tkcolending.example
Address: Suite 5/418 Marlow Avenue Elmvale Vic 3174
Credit Licence No.: 718249

```html
<!DOCTYPE html>
<html lang="en">
<head>
<meta charset="utf-8">
<title>TK &amp; Co Finance Pty Ltd — Business Card</title>
<link href="https://fonts.googleapis.com/css2?family=Montserrat:wght@500;600&family=Open+Sans:ital,wght@0,400;0,700;1,400;1,700&display=swap" rel="stylesheet">
<style>
  :root {
    --page-bg: #e9ecef;
    --brand-blue: #2a7fca;
    --brand-blue-dark: #1f6db5;
    --brand-blue-light: #3c91d8;
    --band-grey: #b9bcbf;
    --card-white: #ffffff;
    --text-white: #ffffff;
  }
  * { box-sizing: border-box; margin: 0; padding: 0; }
  html, body {
    width: 1200px; height: 900px; overflow: hidden;
    background: var(--page-bg);
  }
  .stage {
    width: 1200px; height: 900px;
    display: flex; flex-direction: column;
    align-items: center; justify-content: center; gap: 56px;
  }
  .card {
    position: relative;
    width: 640px; height: 366px;
    border-radius: 4px; overflow: hidden;
    box-shadow: 0 10px 28px rgba(0,0,0,0.18);
  }

  /* Front */
  .card-front {
    background: linear-gradient(135deg, var(--brand-blue-light), var(--brand-blue) 55%, var(--brand-blue-dark));
    color: var(--text-white);
  }
  .card-front .wordmark {
    position: absolute; left: 0; right: 0; top: 140px;
    display: flex; align-items: center; justify-content: center; gap: 14px;
  }
  .wordmark-dot {
    width: 22px; height: 22px; border-radius: 50%;
  }
  .card-front .wordmark-dot { background: var(--text-white); }
  .company-name {
    font-family: "Montserrat", sans-serif; font-weight: 600;
    font-size: 38px; letter-spacing: 0.3px;
  }
  .credit-licence {
    position: absolute; right: 34px; bottom: 30px;
    font-family: "Open Sans", sans-serif; font-size: 15px;
  }

  /* Back */
  .card-back { background: var(--card-white); }
  .back-header {
    height: 150px;
    display: flex; align-items: center; justify-content: center; gap: 14px;
    color: var(--brand-blue);
  }
  .card-back .wordmark-dot { background: var(--brand-blue); }
  .card-back .company-name { font-size: 32px; }
  .back-divider {
    height: 16px;
    background: linear-gradient(var(--page-bg), var(--band-grey));
  }
  .back-body {
    height: 200px;
    background: linear-gradient(135deg, var(--brand-blue-light), var(--brand-blue) 60%, var(--brand-blue-dark));
    color: var(--text-white);
    font-family: "Open Sans", sans-serif;
    display: flex; justify-content: space-between;
    padding: 26px 30px 0 34px;
  }
  .person-name { font-weight: 700; font-style: italic; font-size: 22px; line-height: 1.1; }
  .person-role { font-style: italic; font-size: 18px; margin-top: 2px; }
  .contact-list { list-style: none; width: 300px; padding-top: 36px; }
  .contact-item {
    display: flex; align-items: flex-start; gap: 10px;
    font-size: 15px; line-height: 1.3; margin-bottom: 4px;
  }
  .contact-icon { width: 14px; height: 14px; flex: none; margin-top: 3px; fill: var(--text-white); }
  .contact-email { font-size: 13.5px; white-space: nowrap; }
</style>
</head>
<body>
<main class="stage">
  <section class="card card-front" aria-label="Business card front">
    <div class="wordmark">
      <span class="wordmark-dot"></span>
      <span class="company-name">TK &amp; Co Finance Pty Ltd</span>
    </div>
    <p class="credit-licence">Credit Licence No.: 718249</p>
  </section>

  <section class="card card-back" aria-label="Business card back">
    <header class="back-header">
      <span class="wordmark-dot"></span>
      <span class="company-name">TK &amp; Co Finance Pty Ltd</span>
    </header>
    <div class="back-divider"></div>
    <div class="back-body">
      <div class="person">
        <p class="person-name">Desmond Okafor</p>
        <p class="person-role">Managing Director</p>
      </div>
      <ul class="contact-list">
        <li class="contact-item">
          <svg class="contact-icon" viewBox="0 0 24 24" aria-hidden="true"><path d="M6.6 10.8a15.1 15.1 0 0 0 6.6 6.6l2.2-2.2c.3-.3.7-.4 1-.2 1.1.4 2.3.6 3.6.6.6 0 1 .4 1 1V20c0 .6-.4 1-1 1A17 17 0 0 1 3 4c0-.6.4-1 1-1h3.5c.6 0 1 .4 1 1 0 1.3.2 2.5.6 3.6.1.3 0 .7-.2 1z"/></svg>
          <span>0417 638 294</span>
        </li>
        <li class="contact-item">
          <svg class="contact-icon" viewBox="0 0 24 24" aria-hidden="true"><path d="M6 2h10v6H6zM3 9h18v11H3zm3 3v2h4v-2zm0 4v2h4v-2zm7-4v6h5v-6z"/></svg>
          <span>03 9561 4472</span>
        </li>
        <li class="contact-item">
          <svg class="contact-icon" viewBox="0 0 24 24" aria-hidden="true"><path d="M12 2a10 10 0 1 0 5 18.7l-1-1.7A8 8 0 1 1 20 12v1.5a1.5 1.5 0 0 1-3 0V7h-2v1a5 5 0 1 0 .9 7.3A3.5 3.5 0 0 0 22 13.5V12A10 10 0 0 0 12 2zm0 13a3 3 0 1 1 0-6 3 3 0 0 1 0 6z"/></svg>
          <span class="contact-email">desmond.okafor@tkcolending.example</span>
        </li>
        <li class="contact-item">
          <svg class="contact-icon" viewBox="0 0 24 24" aria-hidden="true"><path d="M12 2a7 7 0 0 0-7 7c0 5.3 7 13 7 13s7-7.7 7-13a7 7 0 0 0-7-7zm0 9.5A2.5 2.5 0 1 1 12 6.5a2.5 2.5 0 0 1 0 5z"/></svg>
          <span>Suite 5/418 Marlow Avenue Elmvale Vic 3174</span>
        </li>
      </ul>
    </div>
  </section>
</main>
</body>
</html>
```